Business Card Design Project

Refresh of logo attached. Require text underneath to be more ledgible, crisper & cleaner.

Overall, staying with same colour scheme need a brighter, crisper, easily readible business card style.

Industry/Entity Type

Business

```html
<!DOCTYPE html>
<html lang="en">
<head>
<meta charset="utf-8">
<title>VERANT business cards</title>
<link href="https://fonts.googleapis.com/css2?family=Jost:wght@300;400;500;700&display=swap" rel="stylesheet">
<style>
  :root {
    --page: #ececec;
    --card-dark: #2c2a2a;
    --card-mid: #363434;
    --card-deep: #232222;
    --blue: #25566d;
    --blue-soft: #2d5f78;
    --blue-light: #7fc3e6;
    --ink: #ffffff;
    --ink-soft: #d9dde0;
  }
  html, body {
    margin: 0;
    width: 1200px;
    height: 848px;
    overflow: hidden;
    background: radial-gradient(ellipse at center, #f6f6f6 0%, var(--page) 75%);
    font-family: "Jost", sans-serif;
  }
  .sheet { position: relative; width: 1200px; height: 848px; }
  .card { position: absolute; width: 479px; height: 293px; display: block; }
  .card--front-a { left: 108px; top: 117px; }
  .card--back-a  { left: 613px; top: 117px; }
  .card--front-b { left: 108px; top: 437px; }
  .card--back-b  { left: 613px; top: 437px; }
  .card text { font-family: "Jost", sans-serif; fill: var(--ink); }
  .brand-name { font-weight: 400; letter-spacing: -1px; }
  .tagline { font-weight: 300; fill: var(--ink-soft); letter-spacing: 0.5px; }
  .tagline-accent { fill: var(--blue-light); }
  .holder-name { font-weight: 700; }
  .holder-title { font-weight: 400; }
  .contact { font-weight: 400; }
  .site { font-weight: 400; letter-spacing: 1px; }
  .fill-dark { fill: var(--card-dark); }
  .fill-mid { fill: var(--card-mid); }
  .fill-deep { fill: var(--card-deep); }
  .fill-blue { fill: var(--blue); }
  .fill-blue-soft { fill: var(--blue-soft); }
  .brand-square { fill: var(--blue-soft); stroke: none; }
  .icon { fill: var(--ink); }
</style>
</head>
<body>
<div class="sheet">

  <!-- Front, layout A -->
  <svg class="card card--front-a" viewBox="0 0 551 337" preserveAspectRatio="none">
    <rect class="fill-dark" width="551" height="337"/>
    <polygon class="fill-mid" points="0,95 285,240 285,337 0,337"/>
    <polygon class="fill-deep" points="285,240 296,240 296,337 285,337"/>
    <polygon class="fill-blue" points="551,0 551,337 288,337 288,245"/>
    <polygon class="fill-blue-soft" points="420,0 551,0 470,80" opacity="0.35"/>
    <rect class="brand-square" x="24" y="32" width="42" height="42"/>
    <text class="brand-name" x="76" y="76" font-size="58">VERANT</text>
    <text class="tagline" x="299" y="42" font-size="15">NATIONAL GUILD</text>
    <text class="tagline" x="299" y="60" font-size="15">OF TRUSTED</text>
    <text class="tagline" x="299" y="78" font-size="15">ESTATE ADVISORS</text>
    <text class="holder-name" x="535" y="184" font-size="29" text-anchor="end">Marek D. Lindqvist</text>
    <text class="holder-title" x="532" y="207" font-size="19" text-anchor="end">Certified Estate Advisor</text>
    <g class="icon">
      <path d="M28,236 h18 v3 h-3 l-2,-3 h-8 l-2,3 h-3z M31,240 h12 l2,8 h-16z"/>
      <circle cx="37" cy="262" r="8" fill="none" stroke="#fff" stroke-width="1.6"/>
      <rect x="28" y="280" width="18" height="12" fill="none" stroke="#fff" stroke-width="1.6"/>
      <path d="M28,280 l9,7 l9,-7" fill="none" stroke="#fff" stroke-width="1.6"/>
      <circle cx="37" cy="308" r="8"/>
    </g>
    <text class="contact" x="52" y="246" font-size="17">(416) 555 0142</text>
    <text class="contact" x="52" y="269" font-size="17">(647) 555 0187</text>
    <text class="contact" x="52" y="292" font-size="17">marek@verant.ca</text>
    <text class="contact" x="52" y="315" font-size="17">www.verant.ca</text>
  </svg>

  <!-- Back, layout A -->
  <svg class="card card--back-a" viewBox="0 0 551 337" preserveAspectRatio="none">
    <rect class="fill-dark" width="551" height="337"/>
    <polygon class="fill-blue" points="0,0 265,0 265,30 0,170"/>
    <polygon class="fill-mid" points="285,0 551,0 551,110 285,20"/>
    <polygon class="fill-blue" points="0,110 120,185 0,250" opacity="0.6"/>
    <polygon class="fill-blue" points="551,110 551,337 288,337 288,280 430,185"/>
    <polygon class="fill-deep" points="275,280 288,280 288,337 275,337"/>
    <rect class="brand-square" x="112" y="120" width="50" height="50"/>
    <text class="brand-name" x="176" y="192" font-size="72">VERANT</text>
    <text class="tagline" x="275" y="222" font-size="11" text-anchor="middle">NATIONAL GUILD OF <tspan class="tagline-accent">TRUSTED ESTATE ADVISORS</tspan></text>
  </svg>

  <!-- Front, layout B -->
  <svg class="card card--front-b" viewBox="0 0 551 337" preserveAspectRatio="none">
    <rect class="fill-dark" width="551" height="337"/>
    <polygon class="fill-mid" points="0,120 140,185 140,337 0,337"/>
    <polygon class="fill-deep" points="0,285 90,337 0,337"/>
    <polygon class="fill-deep" points="140,185 150,185 150,337 140,337"/>
    <polygon class="fill-blue" points="150,185 286,92 286,265 150,337"/>
    <rect class="brand-square" x="24" y="32" width="42" height="42"/>
    <text class="brand-name" x="76" y="76" font-size="58">VERANT</text>
    <text class="tagline" x="299" y="41" font-size="15">NATIONAL GUILD</text>
    <text class="tagline" x="299" y="59" font-size="15">OF TRUSTED</text>
    <text class="tagline" x="299" y="78" font-size="15">ESTATE ADVISORS</text>
    <text class="holder-name" x="529" y="202" font-size="29" text-anchor="end">Marek D. Lindqvist</text>
    <text class="holder-title" x="527" y="225" font-size="19" text-anchor="end">Certified Estate Advisor</text>
    <text class="contact" x="494" y="263" font-size="17" text-anchor="end">(416) 555 0142</text>
    <text class="contact" x="494" y="286" font-size="17" text-anchor="end">(647) 555 0187</text>
    <text class="contact" x="494" y="309" font-size="17" text-anchor="end">marek@verant.ca</text>
    <g class="icon">
      <path d="M502,250 h18 v3 h-3 l-2,-3 h-8 l-2,3 h-3z M505,254 h12 l2,8 h-16z"/>
      <circle cx="511" cy="280" r="8" fill="none" stroke="#fff" stroke-width="1.6"/>
      <rect x="502" y="298" width="18" height="12" fill="none" stroke="#fff" stroke-width="1.6"/>
      <path d="M502,298 l9,7 l9,-7" fill="none" stroke="#fff" stroke-width="1.6"/>
    </g>
  </svg>

  <!-- Back, layout B -->
  <svg class="card card--back-b" viewBox="0 0 551 337" preserveAspectRatio="none">
    <rect class="fill-dark" width="551" height="337"/>
    <polygon class="fill-blue" points="0,0 265,0 265,30 0,170"/>
    <polygon class="fill-mid" points="285,0 551,0 551,110 285,20"/>
    <polygon class="fill-blue" points="0,110 120,185 0,250" opacity="0.6"/>
    <polygon class="fill-blue" points="551,110 551,337 288,337 288,280 430,185"/>
    <polygon class="fill-deep" points="275,280 288,280 288,337 275,337"/>
    <text class="site" x="275" y="168" font-size="38" text-anchor="middle">www.verant.ca</text>
  </svg>

</div>
</body>
</html>
```